Social Media Marketing website

Need website designed for social media marketing company PlumeVista.com
Do no currently have logo.
Pages:
Main
Services
Order
Contact
Please use dummy text for now. I will provide content to winner later to add.
Main page should clearly show the steps with some sort of graphic: Establish, Engage, Analyze.
Services provided (steps):
1) Establish social media presence
2) Social media management and advertising
3) Analyze and engage
Site should be simple, clean and attractive. Design examples:
http://brindlow.com/
http://www.quillmarkhub.com/
http://www.fenwaterlyx.com/
Be creative! It should not look like a template.
Updates
Updated examples.
Contact me for questions.
owen@plumevista.com
3) Analyze and engage
Advertising

```html
<!DOCTYPE html>
<html lang="en">
<head>
<meta charset="utf-8">
<title>Plume Vista — Social Media Marketing</title>
<link href="https://fonts.googleapis.com/css2?family=Noto+Sans:wght@400;700&family=Dancing+Script:wght@600&family=Russo+One&display=swap" rel="stylesheet">
<style>
:root{
  --white:#ffffff;
  --band:#8f979d;
  --band-dark:#7d858b;
  --band-light:#a3aab0;
  --content-bg:#e6ebf3;
  --lower-bg:#fafafa;
  --card-border:#d5dade;
  --ink:#333a40;
  --ink-soft:#555c62;
  --nav:#9aa0a5;
  --link:#2f7fc1;
  --footer:#7f868c;
  --tab:#7e878d;
}
*{box-sizing:border-box;margin:0;padding:0}
html,body{width:1200px;height:1191px;overflow:hidden;background:var(--white)}
body{font-family:"Noto Sans",sans-serif;color:var(--ink)}
.page{position:relative;width:1200px;height:1191px;overflow:hidden}
.abs{position:absolute}

/* header */
.header-top{left:0;top:0;width:1200px;height:63px;background:linear-gradient(#fff,#f1f2f3)}
.hero{left:0;top:63px;width:1200px;height:323px;background:linear-gradient(var(--band) 0%,var(--band-light) 55%,#b9bfc4 100%)}
.logo-tab{left:0;top:40px}
.logo{left:108px;top:34px;font-size:32px;font-weight:700;letter-spacing:1px;color:#5a6268;font-family:"Noto Sans",sans-serif}
.slogan{left:144px;top:70px;font-size:13px;color:#333}
.nav{left:0;top:27px;width:1200px;height:36px}
.nav a{position:absolute;top:0;height:36px;line-height:38px;font-size:15px;color:var(--nav);text-decoration:none;text-transform:uppercase;text-align:center}
.nav a.active{left:528px;width:122px;background:var(--tab);color:#fff;border-radius:3px 3px 0 0;border:1px solid #6d757b;border-bottom:0}
.steps{left:124px;top:128px}
.steps li{list-style:none;display:flex;align-items:center;height:51px;font-family:"Dancing Script",cursive;font-size:25px;color:#fff;text-shadow:1px 1px 2px rgba(0,0,0,.35)}
.steps svg{margin-right:18px}
.btn{top:297px;width:108px;height:26px;background:linear-gradient(#3a3a3a,#000);color:#fff;font-family:"Russo One",sans-serif;font-size:16px;text-align:center;line-height:26px;letter-spacing:1px;border:1px solid #555}
.btn.login{left:129px}.btn.signup{left:248px}
.search-tab{left:0;top:345px}
.search{left:127px;top:358px;width:212px;height:24px;border:1px solid #9aa1a7;border-radius:12px;background:#fff;font-size:13px;color:#8a9096;line-height:22px;padding-left:11px}
.search svg{position:absolute;right:8px;top:4px}
.hero-photo{left:578px;top:93px;width:502px;height:293px;background:linear-gradient(180deg,#8c949a 0%,#d9dcdf 45%,#f3f3f3 100%);border-radius:40px 40px 0 0}

/* services */
.services{left:0;top:386px;width:1200px;height:404px;background:var(--content-bg)}
.card{top:23px;height:347px;background:var(--white);border:4px solid var(--card-border);box-shadow:6px 0 14px rgba(120,135,155,.18)}
.card.c1{left:108px;width:299px}.card.c2{left:451px;width:299px}.card.c3{left:790px;width:299px}
.card-icon{position:absolute;left:14px;top:14px;width:52px;height:52px;border-radius:4px}
.card h2{position:absolute;left:82px;top:16px;width:215px;font-size:17px;font-weight:400;line-height:22px;color:var(--ink)}
.card .body{position:absolute;left:20px;top:80px;width:245px;font-size:13px;line-height:22px;color:var(--ink-soft);text-align:justify}
.card .body p+p{margin-top:22px}
.card ul{list-style:none;margin-top:6px}
.card li{font-size:13px;line-height:26px;color:var(--link);text-align:left;padding-left:18px;position:relative}
.card li::before{content:"";position:absolute;left:2px;top:12px;border-left:5px solid #111;border-top:3px solid transparent;border-bottom:3px solid transparent}
.card li::after{content:"";position:absolute;left:0;top:14px;width:4px;height:1px;background:#111}
.more{position:absolute;font-size:14px;font-weight:700;color:var(--ink);text-decoration:none}
.card .more{left:20px;top:293px}

/* lower */
.lower{left:0;top:790px;width:1200px;height:319px;background:var(--lower-bg)}
.col-title{font-size:18px;font-weight:400;color:var(--ink)}
.why-title{left:167px;top:27px}
.why-icon{left:108px;top:22px}
.why{left:108px;top:80px;width:476px;font-size:11px;line-height:19.5px;color:var(--ink-soft)}
.why .pull{font-weight:700;font-size:12px;line-height:20px;color:#1e2a33;letter-spacing:.4px;margin:8px 0 10px 4px;text-indent:0}
.why .pull span{display:block;padding-left:24px}
.lower .more.why-more{left:109px;top:273px}
.divider{left:598px;top:52px;height:218px;border-left:1px dashed #b5babf}
.test-icon{left:613px;top:22px;width:40px;height:44px;border-radius:50% 50% 8px 8px;background:linear-gradient(#f3b676,#e37c2c)}
.test-title{left:668px;top:27px}
.testimonial{left:613px;width:477px}
.testimonial.t1{top:85px}.testimonial.t2{top:172px}
.thumb{position:absolute;left:0;top:2px;width:67px;height:67px;border:3px solid #d0d4d8;background:#fff}
.thumb span{display:block;width:100%;height:100%}
.testimonial p{margin-left:80px;font-size:11px;line-height:19.5px;color:var(--ink-soft);text-align:justify}

/* footer */
.footer{left:0;top:1109px;width:1200px;height:82px;background:var(--footer);color:#fff}
.footer-links{left:108px;top:20px;font-size:12px}
.footer-links a{color:#fff;text-decoration:none}
.copy{left:108px;top:40px;font-size:11px;letter-spacing:.5px}
.copy u{text-decoration:underline}
.social{left:768px;top:22px;display:flex;gap:4px}
.social a{width:37px;height:41px;background:#fff;border:1px solid #c8ccd0;display:flex;flex-direction:column;align-items:center;justify-content:flex-end;padding-bottom:3px;text-decoration:none;color:#3b5f8a;font-size:6px;line-height:7px}
.social a i{display:block;width:18px;height:18px;background:#9aa3ab;margin-bottom:6px}
</style>
</head>
<body>
<div class="page">

  <header>
    <div class="abs header-top"></div>
    <div class="abs hero"></div>
    <svg class="abs logo-tab" width="400" height="70" viewBox="0 0 400 70">
      <path d="M0 23 H92 C104 23 100 58 140 58 H345 C372 58 370 23 392 23 H400 V0 H0 Z" fill="#ffffff"/>
    </svg>
    <div class="abs logo">PLUME VISTA</div>
    <div class="abs slogan">Company slogan here</div>
    <nav class="abs nav">
      <a class="active" href="#">Home</a>
      <a href="#" style="left:675px;width:120px">Services</a>
      <a href="#" style="left:827px;width:120px">Order</a>
      <a href="#" style="left:980px;width:140px">Contact Us</a>
    </nav>

    <ul class="abs steps">
      <li><svg width="34" height="30" viewBox="0 0 34 30"><path d="M2 16 L8 11 L14 19 L29 2 L33 7 L14 28 Z" fill="#fff" stroke="rgba(0,0,0,.25)" stroke-width="1"/></svg>Establish Social Media Presence</li>
      <li><svg width="34" height="30" viewBox="0 0 34 30"><path d="M2 16 L8 11 L14 19 L29 2 L33 7 L14 28 Z" fill="#fff" stroke="rgba(0,0,0,.25)" stroke-width="1"/></svg>Social Media Management and Advertising</li>
      <li><svg width="34" height="30" viewBox="0 0 34 30"><path d="M2 16 L8 11 L14 19 L29 2 L33 7 L14 28 Z" fill="#fff" stroke="rgba(0,0,0,.25)" stroke-width="1"/></svg>Analyze and Engage</li>
    </ul>
    <a class="abs btn login">LOGIN</a>
    <a class="abs btn signup">SIGN UP</a>

    <svg class="abs search-tab" width="400" height="41" viewBox="0 0 400 41">
      <path d="M95 41 C112 41 108 5 135 5 H350 C375 5 368 41 392 41 Z" fill="#e6ebf3"/>
    </svg>
    <div class="abs search">Enter Your Keyword
      <svg width="22" height="14" viewBox="0 0 22 14"><circle cx="7" cy="6" r="5" fill="none" stroke="#777" stroke-width="1.6"/><path d="M11 9 L18 13" stroke="#777" stroke-width="2"/></svg>
    </div>
    <div class="abs hero-photo" role="img" aria-label="Photo of a marketing team holding up a board showing a social network diagram"></div>
  </header>

  <main>
    <section class="abs services">
      <article class="abs card c1">
        <div class="card-icon" role="img" aria-label="Illustration of computer monitors" style="background:linear-gradient(#d9dde1,#4b5157)"></div>
        <h2>Establish Social Media Presence</h2>
        <div class="body">
          <p>Donec luctus metus a erat ornare sefdlii placerat. Sed metus erat, tincidunt utkloi iaculis sed, pulvinar id eros.</p>
          <p>Pellentesque odio lectus, tincidunt idlioi interdum nec, placerat vitae liberorasliki dui ante, venenatis at adipiscing</p>
        </div>
        <a class="more" href="#">+more...</a>
      </article>
      <article class="abs card c2">
        <div class="card-icon" role="img" aria-label="Illustration of an advertising billboard" style="background:linear-gradient(#7fb3d9,#d59a3a)"></div>
        <h2>Social Media Management and Advertising</h2>
        <div class="body">
          <p>Donec luctus metus a erat ornare sefdlii placerat. Sed metus erat, tincidunt utkloi iaculis sed, pulvinar id eros.</p>
          <ul>
            <li>Nulla vel nisl non turpis vestibulum</li>
            <li>Fusce vulputate magna a velit</li>
            <li>Mauris a felis in nunc luctus pellentes</li>
            <li>Cras sollicitudin justo eget nulla</li>
          </ul>
        </div>
        <a class="more" href="#">+more...</a>
      </article>
      <article class="abs card c3">
        <div class="card-icon" role="img" aria-label="Illustration of a report sheet with a pie chart" style="background:linear-gradient(#f4f5f6,#c9ced3)"></div>
        <h2>Analyze and Engage</h2>
        <div class="body">
          <p>Donec luctus metus a erat ornare sefdlii placerat. Sed metus erat, tincidunt utkloi iaculis sed, pulvinar id eros.</p>
          <ul>
            <li>Nulla vel nisl non turpis vestibulum</li>
            <li>Fusce vulputate magna a velit</li>
            <li>Mauris a felis in nunc luctus pellentes</li>
            <li>Cras sollicitudin justo eget nulla</li>
          </ul>
        </div>
        <a class="more" href="#">+more...</a>
      </article>
    </section>

    <section class="abs lower">
      <svg class="abs why-icon" width="46" height="40" viewBox="0 0 46 40">
        <path d="M2 10 H24 V3 L38 14 L24 25 V18 H2 Z" fill="#3a7fd0"/>
        <path d="M44 26 H22 V19 L8 30 L22 41 V34 H44 Z" fill="#f0962a"/>
      </svg>
      <h3 class="abs col-title why-title">Why Plume Vista</h3>
      <div class="abs why">
        <p>Lorem ipsum dolor sit amet, consectetuer adipiscing elit. Etiam porttitor, lectus ac feugiat pretium, tortor nisi tincidunt nisl.Mauris non mauris at lectus congue varius.</p>
        <p class="pull">lectus ac feugiat pretium. tortor nisi tincidunt nisl.Mauris non<span>mauris at lectus congue varius. Suspendisse faucibus igula ut orci.</span></p>
        <p>Cras vestibulum. Integer dolor urna, porttitor ut.Mauris lacinia. Cras pellentesque bibendum nisi. Cras vestibulum. Integer dolor urnaLorem ipsum dolor sit amet, consectetuer adipiscing elit. Etiam porttitor, lectus ac feugiat pretium, tortor nisi tincidunt nisl.Mauris non mauris at lectus congue varius.</p>
      </div>
      <a class="more why-more" href="#">+more...</a>
      <div class="abs divider"></div>

      <div class="abs test-icon" role="img" aria-label="Icon of a group of people"></div>
      <h3 class="abs col-title test-title">Testimonials</h3>
      <div class="abs testimonial t1">
        <div class="thumb"><span role="img" aria-label="Photo of an office tower" style="background:linear-gradient(#cfd8e0,#7a7f84)"></span></div>
        <p>Lorem ipsum dolor sit amet, consectetuer adipiscing elit. Etiam porttitor, lectus ac feugiat pretium, tortor nisi tincidunt nisl.Mauris non mauris at lectus congue varius.</p>
      </div>
      <div class="abs testimonial t2">
        <div class="thumb"><span role="img" aria-label="Photo of a small orange car" style="background:linear-gradient(#f2f2f2,#e5873c 60%,#bfc3c6)"></span></div>
        <p>Lorem ipsum dolor sit amet, consectetuer adipiscing elit. Etiam porttitor, lectus ac feugiat pretium, tortor nisi tincidunt nisl.Mauris non mauris at lectus congue varius.</p>
      </div>
    </section>
  </main>

  <footer class="abs footer">
    <div class="abs footer-links"><a href="#">Home</a> | <a href="#">Services</a> | <a href="#">Order</a> | <a href="#">Contact Us</a></div>
    <div class="abs copy">© 2011 <u>Plume Vista</u>. All Rights Reserved.</div>
    <div class="abs social">
      <a href="#"><i></i>Clipstream</a>
      <a href="#"><i></i>Markpile</a>
      <a href="#"><i></i>Newsfeed</a>
      <a href="#"><i></i>Chirply</a>
      <a href="#"><i></i>Kinhall</a>
      <a href="#"><i></i>Shutterleaf</a>
      <a href="#"><i></i>Votedock</a>
      <a href="#"><i></i>Wanderpage</a>
    </div>
  </footer>

</div>
</body>
</html>
```